Label for Refill packaging eco-conscious beauty brand

We need a label for our refill pouch. Velvet Harbor is an unscented conditioner formulated using the finest healthy & pure ingredients, free of chemicals and harmful toxins. As a minimalist beauty brand we are proud to be certified with TPL, VerdaSeal and Silver Fawn.

We already have the pouches and an exciting label for our regular bottles.
We choose a kraft brown packing for the refill pouch and would like something minimalist but elegant for the label.

```html
<!DOCTYPE html>
<html lang="en">
<head>
<meta charset="utf-8">
<title>Velvet Harbor refill pouch labels</title>
<link rel="stylesheet" href="https://fonts.googleapis.com/css2?family=Marcellus&family=Montserrat:wght@400;500&display=swap">
<style>
  :root {
    --teal-bg: #045254;
    --label-grey: #cbc8c1;
    --teal-ink: #1f4d52;
    --gold: #c9a23a;
    --gold-light: #e8cf7a;
    --white-ink: #f6f4ef;
    --muted-ink: #9c9a94;
  }
  * { margin: 0; padding: 0; box-sizing: border-box; }
  html, body { width: 1200px; height: 437px; overflow: hidden; }
  body { background: var(--teal-bg); position: relative; font-family: "Montserrat", sans-serif; }

  .label {
    position: absolute;
    top: 164px;
    width: 175px;
    height: 216px;
    background: var(--label-grey);
    display: flex;
    flex-direction: column;
    align-items: center;
  }
  .label--one   { left: 96px; }
  .label--two   { left: 369px; }
  .label--three { left: 669px; }
  .label--four  { left: 947px; }

  .leaf-band {
    width: 100%;
    height: 55px;
    border-bottom: 2px solid var(--gold);
  }
  .leaf-band--teal   { background: linear-gradient(120deg, #3f6a6c, #2f5b5e 45%, #b89a45 70%, #3c6769); }
  .leaf-band--gold   { background: linear-gradient(120deg, #e9d88f, #d7d0b7 40%, #c9a23a 65%, #ede1b0); }
  .leaf-band--silver { background: linear-gradient(120deg, #d9c98a, #c9c7c2 40%, #c9a23a 70%, #e4d9a8); }

  .brand {
    margin-top: 11px;
    display: flex;
    flex-direction: column;
    align-items: center;
    gap: 4px;
  }
  .brand-mark {
    width: 14px;
    height: 14px;
    background: var(--gold);
  }
  .brand-name {
    font-family: "Marcellus", serif;
    font-size: 9px;
    line-height: 1.15;
    color: var(--gold);
    text-align: center;
    letter-spacing: 0.5px;
  }

  .product-name {
    margin-top: 8px;
    font-family: "Marcellus", serif;
    font-size: 14.5px;
    letter-spacing: 0.8px;
    color: var(--white-ink);
    text-transform: uppercase;
    white-space: nowrap;
  }
  .label--two .product-name { color: var(--teal-ink); }

  .rule {
    margin-top: 9px;
    width: 29px;
    height: 2px;
    background: var(--gold);
  }

  .descriptor {
    margin-top: 9px;
    text-align: center;
    font-size: 4.6px;
    letter-spacing: 0.3px;
    line-height: 1.5;
  }
  .descriptor-en { color: var(--teal-ink); font-weight: 500; }
  .descriptor-fr { color: var(--white-ink); }
  .label--two .descriptor-fr { color: var(--teal-ink); }

  .volume {
    margin-top: 6px;
    font-size: 3.8px;
    color: var(--teal-ink);
  }

  .cert-row {
    margin-top: 8px;
    display: flex;
    gap: 13px;
  }
  .cert-badge {
    width: 10px;
    height: 10px;
    border-radius: 50%;
    background: var(--teal-ink);
  }
  .cert-row--light .cert-badge {
    background: transparent;
    border: 1.2px solid var(--white-ink);
  }
  .cert-row--teal .cert-badge {
    background: transparent;
    border: 1.2px solid #2f8a8c;
  }
</style>
</head>
<body>

  <section class="label label--one">
    <div class="leaf-band leaf-band--teal" role="img" aria-label="Gold leaf vein pattern on teal"></div>
    <div class="brand"><span class="brand-mark"></span><span class="brand-name">VERA<br>Linde</span></div>
    <h1 class="product-name">Velvet Harbor</h1>
    <div class="rule"></div>
    <p class="descriptor"><span class="descriptor-en">UNSCENTED HAIR CONDITIONER</span><br><span class="descriptor-fr">APRÈS-SHAMPOING NON PARFUMÉ</span></p>
    <p class="volume">238 ml ℮ 8 Fl. Oz.</p>
    <div class="cert-row"><span class="cert-badge" aria-label="TPL"></span><span class="cert-badge" aria-label="VerdaSeal"></span><span class="cert-badge" aria-label="Silver Fawn"></span></div>
  </section>

  <section class="label label--two">
    <div class="leaf-band leaf-band--teal" role="img" aria-label="Gold leaf vein pattern on teal"></div>
    <div class="brand"><span class="brand-mark"></span><span class="brand-name">VERA<br>Linde</span></div>
    <h1 class="product-name">Velvet Harbor</h1>
    <div class="rule"></div>
    <p class="descriptor"><span class="descriptor-en">UNSCENTED HAIR CONDITIONER</span><br><span class="descriptor-fr">APRÈS-SHAMPOING NON PARFUMÉ</span></p>
    <p class="volume">238 ml ℮ 8 Fl. Oz.</p>
    <div class="cert-row"><span class="cert-badge" aria-label="TPL"></span><span class="cert-badge" aria-label="VerdaSeal"></span><span class="cert-badge" aria-label="Silver Fawn"></span></div>
  </section>

  <section class="label label--three">
    <div class="leaf-band leaf-band--gold" role="img" aria-label="Gold leaf vein pattern on pale cream"></div>
    <div class="brand"><span class="brand-mark"></span><span class="brand-name">VERA<br>Linde</span></div>
    <h1 class="product-name">Velvet Harbor</h1>
    <div class="rule"></div>
    <p class="descriptor"><span class="descriptor-en">UNSCENTED HAIR CONDITIONER</span><br><span class="descriptor-fr">APRÈS-SHAMPOING NON PARFUMÉ</span></p>
    <p class="volume">238 ml ℮ 8 Fl. Oz.</p>
    <div class="cert-row cert-row--light"><span class="cert-badge" aria-label="TPL"></span><span class="cert-badge" aria-label="VerdaSeal"></span><span class="cert-badge" aria-label="Silver Fawn"></span></div>
  </section>

  <section class="label label--four">
    <div class="leaf-band leaf-band--silver" role="img" aria-label="Gold and silver leaf vein pattern"></div>
    <div class="brand"><span class="brand-mark"></span><span class="brand-name">VERA<br>Linde</span></div>
    <h1 class="product-name">Velvet Harbor</h1>
    <div class="rule"></div>
    <p class="descriptor"><span class="descriptor-en">UNSCENTED HAIR CONDITIONER</span><br><span class="descriptor-fr">APRÈS-SHAMPOING NON PARFUMÉ</span></p>
    <p class="volume">238 ml ℮ 8 Fl. Oz.</p>
    <div class="cert-row cert-row--teal"><span class="cert-badge" aria-label="TPL"></span><span class="cert-badge" aria-label="VerdaSeal"></span><span class="cert-badge" aria-label="Silver Fawn"></span></div>
  </section>

</body>
</html>
```